Wedding Invitation Card Design

Design high quality double sided wedding invitation including Monogram, borders matching RSVP cards, Envelope liners and stationary set. Design should be appropriate for printing techniques like gold foiling, edging, letterpress. Size 18 x 12 Rectangle/Horizontal layout.

Preferred color is Gold and matching colors of Gold. Please check attached files for more information.

Target Market(s)

Events

Font styles to use
Serif
Decorative
Script

Colors

Designer to choose colors to be used in the design.

Requirements
Must have
• as described above.
Nice to have
• Excellent borders and monogram.

```html
<!DOCTYPE html>
<html lang="en">
<head>
<meta charset="utf-8">
<title>Wedding Invitation – Nadeesha &amp; Kasun</title>
<link rel="stylesheet" href="https://fonts.googleapis.com/css2?family=Cinzel:wght@500;700&family=Great+Vibes&display=swap">
<style>
  :root {
    --bg-top: #6f6352;
    --bg-bottom: #6a4520;
    --paper: #ebe7df;
    --gold-light: #f1cf55;
    --gold: #d49b25;
    --gold-deep: #9a6412;
    --ink: #2e2a26;
  }
  * { box-sizing: border-box; margin: 0; padding: 0; }
  html, body { width: 1173px; height: 1200px; overflow: hidden; }
  body {
    background: linear-gradient(180deg, var(--bg-top), var(--bg-bottom));
    font-family: "Cinzel", "Times New Roman", serif;
    position: relative;
  }
  .card {
    position: absolute;
    left: 160px;
    width: 860px;
    background: var(--paper);
    box-shadow: 0 6px 18px rgba(0,0,0,.35);
  }
  .card__frame {
    position: absolute; inset: 14px;
    border: 3px solid var(--gold);
    border-image: linear-gradient(90deg, var(--gold-deep), var(--gold-light), var(--gold), var(--gold-light)) 1;
  }
  .card__frame::after {
    content: ""; position: absolute; inset: 5px;
    border: 1px solid var(--gold);
  }
  .gold-text {
    background: linear-gradient(90deg, var(--gold-light), var(--gold) 45%, var(--gold-deep) 70%, var(--gold-light));
    -webkit-background-clip: text; background-clip: text; color: transparent;
  }

  /* Front card */
  .card--front { top: 40px; height: 500px; }
  .wreath {
    position: absolute; left: 140px; top: 90px; width: 580px; height: 270px;
    border-radius: 50% 50% 45% 45% / 60% 60% 40% 40%;
    background: radial-gradient(ellipse at center, var(--gold-deep) 0%, var(--gold) 45%, rgba(212,155,37,.35) 75%, rgba(235,231,223,0) 100%);
  }
  .front__names {
    position: absolute; top: 400px; width: 100%; text-align: center;
    font-size: 25px; font-weight: 700; color: var(--gold);
  }
  .divider { display: block; margin: 0 auto; }
  .front__divider { position: absolute; top: 440px; left: 280px; }
  .front__date {
    position: absolute; top: 458px; width: 100%; text-align: center;
    font-size: 19px; color: var(--gold);
  }

  /* Invitation card */
  .card--invite { top: 520px; height: 640px; text-align: center; color: var(--ink); }
  .monogram {
    display: block; margin: 52px auto 0; width: 66px; height: 62px;
    background: linear-gradient(160deg, var(--gold-light), var(--gold-deep));
    border-radius: 8px;
  }
  .invite__divider { margin-top: 10px; }
  .hosts { margin-top: 12px; font-size: 22px; font-weight: 700; line-height: 1.3; }
  .hosts .small { font-size: 17px; font-weight: 500; display: block; }
  .guest-line {
    width: 700px; margin: 18px auto 0; border-bottom: 1px dashed #555;
  }
  .occasion { margin-top: 18px; font-size: 20px; font-weight: 700; }
  .couple { margin-top: 4px; display: flex; justify-content: center; align-items: baseline; gap: 22px; }
  .couple__name { font-family: "Great Vibes", cursive; font-size: 92px; line-height: 1.05; }
  .couple__and { font-size: 24px; font-weight: 700; }
  .venue { margin-top: 10px; font-size: 16px; font-weight: 700; line-height: 1.3; }
  .ceremony { margin-top: 14px; font-size: 15px; font-weight: 500; }
</style>
</head>
<body>

<section class="card card--front">
  <div class="card__frame"></div>
  <div class="wreath" role="img" aria-label="Gold floral wreath with leaves, flowers and ribbon framing the couple's monogram"></div>
  <h2 class="front__names">Nadeesha &amp; Kasun</h2>
  <svg class="front__divider divider" width="300" height="12" viewBox="0 0 300 12" aria-hidden="true">
    <line x1="4" y1="6" x2="296" y2="6" stroke="#d49b25" stroke-width="1.5"/>
    <circle cx="4" cy="6" r="2.5" fill="#d49b25"/><circle cx="296" cy="6" r="2.5" fill="#d49b25"/>
    <ellipse cx="150" cy="6" rx="12" ry="4" fill="#d49b25"/>
  </svg>
  <p class="front__date">14 November 2019</p>
</section>

<section class="card card--invite">
  <div class="card__frame"></div>
  <div class="monogram" role="img" aria-label="Gold interlaced monogram of the couple's initials"></div>
  <svg class="invite__divider divider" width="240" height="12" viewBox="0 0 240 12" aria-hidden="true">
    <line x1="4" y1="6" x2="236" y2="6" stroke="#b67a1a" stroke-width="1.5"/>
    <circle cx="4" cy="6" r="2.5" fill="#b67a1a"/><circle cx="236" cy="6" r="2.5" fill="#b67a1a"/>
    <ellipse cx="120" cy="6" rx="10" ry="4" fill="#b67a1a"/>
  </svg>
  <div class="hosts">
    Mr and Mrs Ruwan Dissanayake
    <span class="small">together with</span>
    Mr and Mrs Lalith Fernando<br>
    request the pleasure of the company of
  </div>
  <div class="guest-line"></div>
  <p class="occasion">at the marriage of their children</p>
  <div class="couple">
    <span class="couple__name gold-text">Nadeesha</span>
    <span class="couple__and">and</span>
    <span class="couple__name gold-text">Kasun</span>
  </div>
  <p class="venue">
    at The Grand Ballroom Lotus Bay Hotel Colombo, Sri Lanka<br>
    on Thursday 14th November 2019 at 6.00pm onwards
  </p>
  <p class="ceremony">(Poruwa ceremony will commence at 06.20pm)</p>
</section>

</body>
</html>
```